interior designer/stylist looking for a letter press business card to reflect the stylish work

Hello Designers,
I need a business card design for an company called Halvard Interior Design. I'm aiming at the high end residential and private client market in London providing sleek simple interiors. I'd like my business card to be tackboard worthy and expensive looking, i want people to pin it and for it to have a sought after look, and want prospective customers to hire me as their interior designer as my card is so beautiful.
I love letter press design. I also like the use of colour/foil on the edge.
Colour combos & general things I like -
Black and White
Navy Blue and Gold
Neutral colours (muted palette of greys whites navys beiges)
White Marble & brass
Morvane (fashion designer)
....also open to other suggestions....
Please dont take the pink in the attached photos too literally. i'd like the card to look more masculine than feminine.
I'd like Halvard on one side in one font, with interior design underneath so one word will make the statement....... unless anyone has any other ideas, open to suggestions.
I'd like a really simple font and for the whole card to look very graphic.
my details -
Petra Quillby
Interior Designer & Stylist
email petra@halvardinteriordesign.co.uk
phone +447813554019
website wwww.halvardinteriordesign.co.uk
GO GO GO!! EXCITED TO SEE THE OUTCOME!!
x L
Target Market(s)
High End Residential and private clients
Industry/Entity Type
Business
Contact Information for Business Card
Halvard Interior Design & Styling
Petra Quillby
phone +447813554019

```html
<!DOCTYPE html>
<html lang="en">
<head>
<meta charset="utf-8">
<title>Petra Quillby — Business Card</title>
<link href="https://fonts.googleapis.com/css2?family=Pirata+One&family=Tinos&display=swap" rel="stylesheet">
<style>
  :root {
    --backdrop: #3a332c;
    --card: #050505;
    --gold: #e0a12c;
    --ink-light: #f2f2f2;
    --ink-shadow: #8a8a8a;
  }
  * { margin: 0; padding: 0; box-sizing: border-box; }
  html, body { width: 1200px; height: 750px; overflow: hidden; }
  body { background: var(--backdrop); }
  .stage { position: relative; width: 1200px; height: 750px; }

  .card {
    position: absolute;
    top: 30px;
    width: 460px;
    height: 690px;
    background: var(--card);
  }
  .card--front { left: 66px; }
  .card--back { left: 690px; }

  .display {
    font-family: "Pirata One", "Times New Roman", serif;
    font-weight: 400;
    white-space: nowrap;
  }

  /* Front */
  .front-name {
    position: absolute;
    left: 18px; top: 10px;
    font-size: 40px;
    font-style: italic;
    color: var(--ink-light);
    text-shadow: 3px 3px 0 var(--ink-shadow);
    letter-spacing: 1px;
  }
  .front-rule {
    position: absolute;
    left: 0; right: 0; top: 68px;
    height: 2px;
    background: var(--gold);
  }
  .front-title {
    position: absolute;
    left: 0; right: 0; top: 228px;
    text-align: center;
    font-size: 44px;
    color: var(--gold);
    text-shadow: 2px 3px 0 #6b4a10;
  }
  .contact {
    position: absolute;
    left: 18px; top: 456px;
    font-family: "Tinos", "Times New Roman", serif;
    color: var(--ink-light);
    font-size: 23px;
    line-height: 37px;
    list-style: none;
  }
  .contact .phone { font-size: 26px; }
  .front-edge {
    position: absolute;
    left: 442px; top: 450px;
    width: 3px; height: 240px;
    background: var(--gold);
  }

  /* Back */
  .brand {
    position: absolute;
    left: 0; right: 0; top: 92px;
    display: flex;
    align-items: center;
    justify-content: center;
    gap: 18px;
  }
  .brand-mark {
    width: 46px; height: 46px;
    background: var(--gold);
  }
  .brand-name {
    font-size: 72px;
    color: var(--gold);
  }
  .back-name {
    position: absolute;
    left: 0; right: 0; top: 378px;
    text-align: center;
    font-size: 62px;
    font-style: italic;
    color: var(--ink-light);
    text-shadow: 3px 4px 0 var(--ink-shadow);
  }
  .back-title {
    position: absolute;
    left: 0; right: 0; top: 494px;
    text-align: center;
    font-size: 44px;
    color: var(--ink-light);
    text-shadow: 3px 3px 0 var(--ink-shadow);
  }
  .back-company {
    position: absolute;
    left: 0; right: 0; top: 590px;
    text-align: center;
    font-size: 33px;
    color: var(--ink-light);
    text-shadow: 3px 3px 0 var(--ink-shadow);
  }
</style>
</head>
<body>
<main class="stage">
  <section class="card card--front">
    <h1 class="front-name display">Petra Quillby</h1>
    <div class="front-rule"></div>
    <p class="front-title display">Interior Designer &amp; Stylist</p>
    <ul class="contact">
      <li>petra@halvardinteriordesign.co.uk</li>
      <li>wwww.halvardinteriordesign.co.uk</li>
      <li class="phone">phone +447813554019</li>
    </ul>
    <div class="front-edge"></div>
  </section>

  <section class="card card--back">
    <div class="brand">
      <span class="brand-mark"></span>
      <span class="brand-name display">Halvard</span>
    </div>
    <h2 class="back-name display">Petra Quillby</h2>
    <p class="back-title display">Interior Designer &amp; Stylist</p>
    <p class="back-company display">Halvard Interior Design &amp; Styling</p>
  </section>
</main>
</body>
</html>
```